Meridale Counsel Corp Business Card design and layout

Meridale Counsel is a small, professional advisory firm specializing in business process consulting and advisory services. We are focused in the energy sector. The business card is to have a combination of blue shades and be professional and serious in nature. Investment banking, capital management, and professional service company card layouts should be used for similar templates

Target Market(s)

Medium to major corporations.

Industry/Entity Type

Consulting

Contact Information for Business Card

The card is to be professional looking in nature and must incorporate the company logo and name in some manner. A two sided design where the opposite side has a QR code and the logo is required.

Logo Text

Brastonhill Partners Inc.

Colors
0592cd
0455a3
3276b5
33a6d7
85cae6
85abd2
cee9f5
cedeed
ecf7fb

Requirements
Must have
• The card is to be professional and have space for employee, title, address, website, and phone numbers (office and cell). The layout must be some shades of blue.
Nice to have
• A space for embossing and/or some subtle gold highlights
Should not have
• Rainbow colours, unprofessional looking fonts (scribble, cursive writing)

```html
<!DOCTYPE html>
<html lang="en">
<head>
<meta charset="utf-8">
<title>Meridale Counsel Corp – Business Card</title>
<link rel="stylesheet" href="https://fonts.googleapis.com/css2?family=Open+Sans:wght@400;600;700&display=swap">
<style>
  :root {
    --page-bg: #e9ecef;
    --card-white: #ffffff;
    --sky-blue: #33a6d7;
    --navy: #2b2b91;
    --logo-navy: #2c3e9a;
    --accent-gold: #e9a23b;
    --text-light: #ffffff;
    --qr-fill: #e6e8f5;
    --shadow: rgba(20, 30, 60, 0.25);
  }
  html, body {
    margin: 0;
    padding: 0;
    width: 1200px;
    height: 911px;
    overflow: hidden;
    background: var(--page-bg);
    font-family: "Open Sans", Arial, sans-serif;
  }
  .canvas {
    position: relative;
    width: 1200px;
    height: 911px;
  }
  .card {
    position: absolute;
    top: 301px;
    width: 540px;
    height: 309px;
    box-shadow: 0 8px 24px var(--shadow);
    overflow: hidden;
  }
  .card-front { left: 40px; background: var(--card-white); }
  .card-back  { left: 620px; background: var(--navy); }

  .front-art {
    position: absolute;
    inset: 0;
  }
  .contact-block {
    position: absolute;
    left: 26px;
    top: 84px;
    color: var(--text-light);
    line-height: 1.35;
  }
  .person-name {
    font-size: 17px;
    font-weight: 700;
    margin: 0;
    letter-spacing: 0.2px;
  }
  .person-title {
    font-size: 12px;
    font-weight: 400;
    margin: 0 0 10px;
    letter-spacing: 0.5px;
  }
  .address-line, .contact-line {
    font-size: 12px;
    margin: 0;
  }
  .address-line:last-of-type { margin-bottom: 6px; }
  .contact-line {
    display: flex;
    align-items: center;
    gap: 7px;
  }
  .contact-line svg { width: 11px; height: 11px; flex: none; }

  .brand-front {
    position: absolute;
    right: 34px;
    top: 116px;
    display: flex;
    align-items: center;
    gap: 10px;
  }
  .brand-square {
    width: 18px;
    height: 18px;
    background: var(--sky-blue);
    flex: none;
  }
  .brand-name {
    font-size: 24px;
    font-weight: 600;
    color: var(--logo-navy);
    line-height: 1.1;
    margin: 0;
  }

  .back-url {
    position: absolute;
    left: 30px;
    top: 50%;
    transform: translate(-50%, -50%) rotate(90deg);
    margin: 0;
    color: var(--text-light);
    font-size: 12px;
    letter-spacing: 1.5px;
    white-space: nowrap;
  }
  .brand-back {
    position: absolute;
    left: 70px;
    top: 50%;
    transform: translateY(-50%);
    display: flex;
    align-items: center;
    gap: 12px;
  }
  .brand-back .brand-square { background: var(--text-light); width: 22px; height: 22px; }
  .brand-back .brand-name { color: var(--text-light); font-size: 26px; white-space: nowrap; }
  .qr-code {
    position: absolute;
    right: 36px;
    top: 50%;
    transform: translateY(-50%);
    width: 96px;
    height: 96px;
    background: var(--qr-fill);
  }
</style>
</head>
<body>
<main class="canvas">

  <section class="card card-front" aria-label="Business card front">
    <svg class="front-art" viewBox="0 0 540 309" width="540" height="309" aria-hidden="true">
      <defs>
        <linearGradient id="panelBlue" x1="0" y1="0" x2="1" y2="1">
          <stop offset="0" stop-color="#5bbbe3"/>
          <stop offset="1" stop-color="#2f9fd2"/>
        </linearGradient>
      </defs>
      <path d="M0 0 H228 C300 90 300 215 205 309 H0 Z" fill="url(#panelBlue)"/>
      <path d="M214 309 C308 220 310 110 258 38" fill="none" stroke="#e9a23b" stroke-width="7" stroke-linecap="round"/>
      <path d="M236 44 L250 12 L276 40 Z" fill="#e9a23b"/>
    </svg>

    <div class="contact-block">
      <p class="person-name">DANIEL ASHCOMBE, P.ENG</p>
      <p class="person-title">PRESIDENT</p>
      <p class="address-line">310, 847-14 th Ave, SW</p>
      <p class="address-line">Calgary, AB T3K 2M5</p>
      <p class="contact-line">
        <svg viewBox="0 0 12 12"><path d="M2 1 L4.5 1 L5.5 3.5 L4 4.8 C4.8 6.5 5.5 7.2 7.2 8 L8.5 6.5 L11 7.5 L11 10 C6 11 1 6 2 1 Z" fill="#fff"/></svg>
        O: 403-555-0142
      </p>
      <p class="contact-line">
        <svg viewBox="0 0 12 12"><rect x="3" y="0.5" width="6" height="11" rx="1.2" fill="#fff"/><rect x="4" y="2" width="4" height="6.5" fill="#33a6d7"/></svg>
        C: 403-555-0187
      </p>
      <p class="contact-line">
        <svg viewBox="0 0 12 12"><rect x="1" y="2.5" width="10" height="7" fill="#fff"/><path d="M1 2.5 L6 6.5 L11 2.5" fill="none" stroke="#33a6d7" stroke-width="1"/></svg>
        dashcombe@meridalecounselcorp.com
      </p>
      <p class="contact-line">
        <svg viewBox="0 0 12 12"><circle cx="6" cy="6" r="5" fill="#fff"/><path d="M1 6 H11 M6 1 C3.5 4 3.5 8 6 11 M6 1 C8.5 4 8.5 8 6 11" fill="none" stroke="#33a6d7" stroke-width="0.8"/></svg>
        www.meridalecounselcorp.com
      </p>
    </div>

    <div class="brand-front">
      <span class="brand-square"></span>
      <p class="brand-name">Meridale<br>Counsel Corp</p>
    </div>
  </section>

  <section class="card card-back" aria-label="Business card back">
    <p class="back-url">www.meridalecounselcorp.com</p>
    <div class="brand-back">
      <span class="brand-square"></span>
      <p class="brand-name">Meridale Counsel Corp</p>
    </div>
    <div class="qr-code" role="img" aria-label="QR code linking to the company website"></div>
  </section>

</main>
</body>
</html>
```